Business Card Ayurvedic Massage

I'm starting with my ayurvedic massage business and need a business card design. The design should be inline with my brand/logo as well as with the design of my website (www.lumo-thara.ch).
Front: logo and text "Ayurvedische Massagen"
back: name and adress (see details https://www.lumo-thara.ch/kontakt.html)

```html
<!DOCTYPE html>
<html lang="de">
<head>
<meta charset="utf-8">
<title>lumo-thara – Visitenkarte</title>
<link href="https://fonts.googleapis.com/css2?family=Lato:wght@400;700&display=swap" rel="stylesheet">
<style>
  :root {
    --stage: #a0a0a0;
    --paper: #ffffff;
    --maroon: #6e0c19;
    --maroon-deep: #7a1420;
    --gold: #d9a22e;
    --gold-light: #f0c24e;
    --ink: #222222;
  }
  * { box-sizing: border-box; margin: 0; padding: 0; }
  html, body { width: 1200px; height: 900px; overflow: hidden; }
  body {
    position: relative;
    background: var(--stage);
    font-family: "Lato", sans-serif;
    color: var(--ink);
  }
  .card {
    position: absolute;
    top: 200px;
    width: 310px;
    height: 502px;
    box-shadow: 3px 4px 6px rgba(0,0,0,0.35);
  }
  .card--contact {
    left: 253px;
    background: var(--paper);
    border-radius: 62px 0 62px 0;
  }
  .card--brand {
    left: 627px;
    background: var(--maroon);
    border-radius: 0 62px 0 62px;
  }
  .elephant {
    position: absolute;
    border-radius: 8px;
    background: radial-gradient(circle at 50% 55%, #b8242c 0%, #8a1a22 45%, #e0a534 75%, rgba(224,165,52,0) 100%);
  }
  .card--contact .elephant { top: 112px; width: 68px; height: 86px; }
  .elephant--left { left: 24px; }
  .elephant--right { left: 217px; }
  .card--brand .elephant {
    left: 93px; width: 108px; height: 80px;
    background: radial-gradient(circle at 50% 50%, #d05a3a 0%, #e0a534 50%, rgba(224,165,52,0.15) 100%);
  }
  .elephant--top { top: 105px; }
  .elephant--bottom { top: 335px; }
  .wordmark {
    position: absolute;
    font-family: "Lato", sans-serif;
    font-weight: 700;
    letter-spacing: 0.5px;
    white-space: nowrap;
  }
  .card--contact .wordmark {
    left: 96px; top: 150px;
    font-size: 17px;
    color: var(--maroon-deep);
  }
  .card--brand .wordmark {
    left: 163px; top: 260px;
    font-size: 24px;
    color: var(--gold-light);
    transform: translate(-50%, -50%) rotate(-90deg);
  }
  .person {
    position: absolute;
    left: 32px; top: 300px;
  }
  .person__name {
    font-size: 18px;
    font-weight: 700;
    color: var(--gold);
    letter-spacing: 0.2px;
  }
  .person__role { font-size: 14px; margin-top: 1px; }
  .contact-list {
    list-style: none;
    position: absolute;
    left: 33px; top: 346px;
    font-size: 14px;
    line-height: 18.5px;
  }
  .contact-list li { display: flex; align-items: center; gap: 5px; }
  .contact-list svg { width: 11px; height: 11px; fill: var(--gold); flex: none; }
  .address {
    position: absolute;
    left: 33px; top: 410px;
    font-size: 14px;
    line-height: 18.5px;
    font-style: normal;
  }
</style>
</head>
<body>
  <section class="card card--contact">
    <div class="elephant elephant--left" role="img" aria-label="Geschmückter Elefant mit Schirm, Illustration"></div>
    <span class="wordmark">lumo-thara</span>
    <div class="elephant elephant--right" role="img" aria-label="Geschmückter Elefant mit Schirm, Illustration"></div>

    <div class="person">
      <p class="person__name">DANIEL BRENNER</p>
      <p class="person__role">Managing Director</p>
    </div>

    <ul class="contact-list">
      <li>
        <svg viewBox="0 0 12 12" aria-hidden="true"><path d="M1 4c0-2 2-3 5-3s5 1 5 3v1H8.5V3.8H3.5V5H1z M2.5 6h7l1 5h-9z"/></svg>
        +41 77 555 01 23
      </li>
      <li>
        <svg viewBox="0 0 12 12" aria-hidden="true"><path d="M0 2h12v8H0z" /><path d="M0 2l6 4.5L12 2" fill="none" stroke="#fff" stroke-width="1"/></svg>
        info@lumo-thara.ch
      </li>
      <li>
        <svg viewBox="0 0 12 12" aria-hidden="true"><circle cx="6" cy="6" r="5.5"/><path d="M3 4.5c1-1 2 0 2.5 1S4 8 5 9.5M7.5 2.5c.5 1 2 1 2.5 2.5-1 0-1.5 1-1 2" fill="none" stroke="#fff" stroke-width="0.9"/></svg>
        www.lumo-thara.ch
      </li>
    </ul>

    <address class="address">
      Nora Keller, lumo-thara<br>
      Lindenweg 14<br>
      8855 Wangen (SZ)
    </address>
  </section>

  <section class="card card--brand">
    <div class="elephant elephant--top" role="img" aria-label="Geschmückter Elefant mit Schirm in Gold, Illustration"></div>
    <span class="wordmark">lumo-thara</span>
    <div class="elephant elephant--bottom" role="img" aria-label="Geschmückter Elefant mit Schirm in Gold, Illustration"></div>
  </section>
</body>
</html>
```